Startup company business card (Media & Advertising)

we need a business card design for a company that is a startup in the media and aggregation industry. Card needs to look funky and of a new breed/modern and upmarket.

Target Market(s)

advertisers/ brand agencies & media publishers

Industry/Entity Type

Advertising

Contact Information for Business Card

Please ensure the front face signifies our brand (plintovo.com) and back has details for the contact. Standard contact such as phone , address, email , website etc.

Font styles to use
Other font styles liked:
• use styleguide and logo font and color

Colors

Designer to choose colors to be used in the design.

Requirements
Must have
• We are disrupting the media and agency industry so subtlety would be good to use imagery to signify this
Nice to have
• Please use logo colors for branding
Should not have
• be as creative and provide few options. Pick a brand color from logo and styleguide

```html
<!DOCTYPE html>
<html lang="en">
<head>
<meta charset="utf-8">
<title>plintovo business card</title>
<link href="https://fonts.googleapis.com/css2?family=Lato:wght@300;400;700;900&display=swap" rel="stylesheet">
<style>
  :root {
    --brand-red: #ea4452;
    --brand-red-deep: #c8283f;
    --map-red: #d6374a;
    --ink: #111111;
    --paper: #ffffff;
    --muted: #4a4a4a;
    --stage: #e9e9ec;
  }
  * { box-sizing: border-box; margin: 0; padding: 0; }
  html, body { width: 1200px; height: 900px; overflow: hidden; }
  body {
    background: var(--stage);
    font-family: "Lato", sans-serif;
    display: flex;
    align-items: center;
    justify-content: center;
    gap: 40px;
  }
  .card {
    position: relative;
    width: 560px;
    height: 320px;
    overflow: hidden;
    box-shadow: 0 10px 30px rgba(0,0,0,0.18);
  }

  /* Front */
  .card-front { background: var(--brand-red); }
  .world-map {
    position: absolute;
    left: 80px; top: 36px;
    width: 420px; height: 190px;
    border-radius: 40px;
    background: radial-gradient(ellipse at center, #cf3247 0%, rgba(214,55,74,0.55) 60%, rgba(234,68,82,0) 100%);
  }
  .front-brand {
    position: absolute;
    left: 0; right: 0; top: 100px;
    display: flex; align-items: center; justify-content: center; gap: 16px;
  }
  .brand-dot {
    width: 46px; height: 46px; border-radius: 50%;
    background: var(--ink);
  }
  .brand-name {
    font-weight: 900;
    font-size: 56px;
    letter-spacing: 1px;
    color: var(--ink);
    line-height: 1;
  }
  .front-tagline {
    position: absolute; left: 0; right: 0; top: 212px;
    text-align: center;
    font-size: 13px; font-weight: 700; letter-spacing: 0.5px;
    color: var(--ink);
  }
  .front-url {
    position: absolute; left: 0; right: 0; top: 238px;
    text-align: center;
    font-size: 13px; font-weight: 700;
    color: var(--paper);
  }

  /* Back */
  .card-back { background: var(--paper); }
  .back-wave { position: absolute; inset: 0; }
  .back-brand {
    position: absolute; left: 150px; top: 44px;
    display: flex; align-items: center; gap: 14px;
  }
  .back-brand .brand-dot { width: 40px; height: 40px; background: var(--brand-red); }
  .back-brand .brand-name { font-size: 46px; }
  .holder {
    position: absolute; left: 40px; top: 128px; width: 230px; text-align: right;
  }
  .holder-name { font-size: 19px; font-weight: 700; color: var(--brand-red); }
  .holder-role { font-size: 12px; font-weight: 300; color: var(--muted); margin-top: 2px; }
  .holder-address {
    margin-top: 22px;
    font-size: 12px; font-weight: 700; line-height: 1.45;
    color: var(--brand-red);
  }
  .divider {
    position: absolute; left: 292px; top: 118px;
    width: 2px; height: 110px;
    background: linear-gradient(to bottom, rgba(0,0,0,0), #777 50%, rgba(0,0,0,0));
  }
  .contact-list {
    position: absolute; left: 312px; top: 124px;
    list-style: none;
  }
  .contact-list li {
    display: flex; align-items: center; gap: 10px;
    font-size: 13px; color: var(--muted);
    margin-bottom: 10px;
  }
  .contact-list svg { width: 14px; height: 14px; fill: var(--brand-red); flex: none; }
</style>
</head>
<body>

  <section class="card card-front" aria-label="Card front">
    <div class="world-map" role="img" aria-label="Dotted world map in deeper red"></div>
    <div class="front-brand">
      <span class="brand-dot"></span>
      <span class="brand-name">plintovo</span>
    </div>
    <p class="front-tagline">REACH EVERY SCREEN, EVERY DAY!</p>
    <p class="front-url">www.plintovo.com</p>
  </section>

  <section class="card card-back" aria-label="Card back">
    <svg class="back-wave" viewBox="0 0 560 320" preserveAspectRatio="none" aria-hidden="true">
      <path d="M40 320 C170 230 360 300 560 110 L560 320 Z" fill="var(--brand-red-deep)"/>
      <path d="M70 320 C200 250 380 300 560 140 L560 320 Z" fill="var(--brand-red)"/>
      <path d="M120 320 C240 270 400 300 560 170 L560 320 Z" fill="var(--paper)"/>
    </svg>

    <div class="back-brand">
      <span class="brand-dot"></span>
      <span class="brand-name">plintovo</span>
    </div>

    <div class="holder">
      <p class="holder-name">Mara Kessel</p>
      <p class="holder-role">Law Attorney</p>
      <p class="holder-address">42 Harlow Lane, Suite 310<br>Brightmoor, QX 40218</p>
    </div>

    <div class="divider"></div>

    <ul class="contact-list">
      <li>
        <svg viewBox="0 0 16 16"><path d="M1 6 C1 3 15 3 15 6 L15 8 L11 8 L11 6.5 C9 5.8 7 5.8 5 6.5 L5 8 L1 8 Z M4 9 L12 9 L14 14 L2 14 Z"/></svg>
        (555) 013-4820
      </li>
      <li>
        <svg viewBox="0 0 16 16"><path d="M4 1 H12 V5 H4 Z M1 6 H15 V12 H12 V10 H4 V12 H1 Z M5 11 H11 V15 H5 Z"/></svg>
        (555) 017-2396
      </li>
      <li>
        <svg viewBox="0 0 16 16"><path d="M1 3 H15 V13 H1 Z M2 4 L8 9 L14 4" stroke="#fff" stroke-width="1.2"/></svg>
        mara@plintovo.com
      </li>
    </ul>
  </section>

</body>
</html>
```